The Quiet Lantern - The best guide in your pocket

The Quiet Lantern (فانوس‌آرام in Persian)

We need a new app design for a major update on Android, iOS and Windows Universal platforms.
Our company works on creating innovative apps and games on different platforms, this particular app is free for end users and provides location based services. Here is the abstract feature list:
• Nearest points around user (explore on map or find) including locations, events and skills
• Add points to our database (partners) plus comments and ratings
• Point owners can modify or complete their points data, provide sale events, services and …

Attachments:
Our service logo
The detailed descriptions of different sections (PDF documents)
Updates

Project Deadline Extended Reason: We want more designs :)Give us previews on Home and Map sections at least (more interesting if previews are provided for more sections) Added Saturday, January 7, 2017

Target Market(s)

Public

Industry/Entity Type

Android

Font styles to use
Serif
Sans Serif

Requirements
Must have
• Consider attached service logo & wireframe
• Designs for attached sections
• Fluent user experience
• Modern design
Nice to have
• Right to Left layouts
Should not have
• No alphabet in graphic assets

```html
<!DOCTYPE html>
<html lang="en">
<head>
<meta charset="utf-8">
<title>The Quiet Lantern – App Screens</title>
<link href="https://fonts.googleapis.com/css2?family=Roboto+Condensed:wght@400;700&family=Vazirmatn:wght@700&display=swap" rel="stylesheet">
<style>
:root{
  --stage:#3d5a6b;
  --teal:#3fb3a4;
  --teal-soft:#79c9bf;
  --teal-mute:#6fa7a6;
  --slate:#3e5663;
  --screen-top:#e3f5f2;
  --screen-bottom:#8fd6cc;
  --ink:#2f4550;
  --ink-soft:#4f6d72;
  --paper:#ffffff;
  --line:#d7e2e2;
}
*{box-sizing:border-box;margin:0;padding:0}
html,body{width:1200px;height:697px;overflow:hidden;background:var(--stage)}
body{position:relative;font-family:"Roboto Condensed",Arial,sans-serif;color:var(--ink)}
.screen{position:absolute;width:138px;height:246px;overflow:hidden;
  background:linear-gradient(170deg,var(--screen-top) 0%,#bfe9e2 55%,var(--screen-bottom) 100%)}
.row-top{top:80px}.row-bottom{top:356px}
.status{position:absolute;top:0;left:0;width:100%;height:10px;background:var(--paper);
  font-size:5px;line-height:10px;color:#222;padding:0 5px;display:flex;justify-content:space-between}
.battery{display:inline-block;width:8px;height:4px;border:0.6px solid #222;vertical-align:middle;margin-left:1px;position:relative}
.battery::before{content:"";position:absolute;left:0;top:0;height:100%;width:25%;background:#222}
.abs{position:absolute;left:6px;width:126px}
.btn{height:20px;line-height:20px;text-align:center;color:#fff;font-size:7px;font-weight:700;text-transform:uppercase}
.btn.teal{background:var(--teal)}
.btn.slate{background:var(--slate)}
.head{height:14px;line-height:14px;background:var(--teal);color:#fff;text-align:center;font-size:7px;font-weight:700}
.bar{height:12px;line-height:12px;background:var(--slate);color:#fff;font-size:5px;font-weight:700;padding-left:6px;text-transform:uppercase}
.bar.light{background:var(--teal)}
.bar::after{content:"";position:absolute;right:6px;top:5px;border:2px solid transparent;border-top:2.5px solid #fff}
.list{background:var(--paper);padding:1px 6px}
.list span{display:block;font-size:4px;line-height:8px;color:#555;border-bottom:0.5px solid var(--line)}
.field{height:12px;line-height:12px;font-size:4.5px;color:#fff;padding-left:6px;border-bottom:0.5px solid rgba(255,255,255,.35);position:relative}
.field::after{content:"";position:absolute;right:6px;top:5px;border:2px solid transparent;border-top:2.5px solid #fff}
.fields.dark{background:#5f8d92}
.fields.tealish{background:var(--teal-soft)}
.brand{position:absolute;top:24px;left:0;width:100%;text-align:center;font-family:"Vazirmatn",sans-serif;font-weight:700;font-size:15px;color:var(--slate);direction:rtl}
.brand .dot{display:inline-block;width:10px;height:10px;border-radius:50%;background:var(--slate);vertical-align:middle;margin-left:4px}
.input{height:20px;background:var(--paper);font-size:5.5px;line-height:20px;color:#999;padding-left:7px;position:relative}
.input svg{position:absolute;right:6px;top:5px}
.map{position:absolute;left:0;width:100%;background:linear-gradient(135deg,#f3e6a8,#9fd3a0 45%,#e7d78c 70%,#b9e0d6)}
.photo{position:absolute;background:linear-gradient(150deg,#6b7b78,#9aa8a0 40%,#2e3a38 75%,#c65a4a)}
.para{font-size:4.3px;line-height:5.6px;color:var(--ink-soft);text-align:left}
.center{text-align:center}
.title{font-size:8px;color:var(--ink);text-transform:uppercase}
.trio{display:flex;gap:2px}
.trio div{flex:1;height:12px;line-height:12px;background:var(--slate);color:#fff;font-size:4.3px;text-align:center;font-weight:700}
.cats div{height:15.4px;line-height:14px;font-size:5.5px;color:#2b7f79;padding-left:22px;border-bottom:0.6px solid rgba(255,255,255,.7);position:relative}
.cats div::before{content:"";position:absolute;left:6px;top:4px;width:6px;height:6px;border-radius:1px;background:var(--teal)}
.cats div::after{content:"";position:absolute;right:4px;top:5px;border:2px solid transparent;border-left:2.5px solid #6c8a8e}
.feat{position:absolute;left:4px;width:130px;height:20px}
.feat .ico{position:absolute;left:0;top:0;width:20px;height:20px;background:var(--slate);display:flex;align-items:center;justify-content:center}
.feat .ico i{width:10px;height:10px;border-radius:50%;border:1.5px solid #fff}
.feat p{position:absolute;left:24px;top:0;width:106px;font-size:4.2px;line-height:5.2px;color:var(--ink)}
.cards{display:flex;justify-content:center;gap:2px}
.cards span{width:28px;height:16px;border-radius:1.5px;background:var(--paper);box-shadow:0 0 0 0.5px #b9c8c8}
.cards span:nth-child(2){background:#f3f3f3}
.cards span:nth-child(3){background:#4a8fd0}
.stats{display:flex}
.stats div{flex:1;text-align:center;color:var(--ink)}
.stats div+div{border-left:0.6px solid #aacfca}
.stats b{display:block;font-size:5px}
.stats strong{display:block;font-size:10px;font-weight:700}
</style>
</head>
<body>

<!-- Row 1 -->
<section class="screen row-top" style="left:106px" aria-label="Login">
  <div class="status"><span>●●●○○ LUMA</span><span>4:21 PM</span><span>22%<i class="battery"></i></span></div>
  <div class="brand"><span>فانوس‌آرام</span><span class="dot"></span></div>
  <div class="abs input" style="top:134px">Phone Number
    <svg width="8" height="9" viewBox="0 0 8 9"><circle cx="4" cy="2.5" r="2" fill="#9aa"/><path d="M0 9 Q4 3 8 9Z" fill="#9aa"/></svg></div>
  <div class="abs input" style="top:158px">Verification Code
    <svg width="7" height="9" viewBox="0 0 7 9"><rect x="0" y="4" width="7" height="5" fill="#9aa"/><path d="M1.5 4V2.5a2 2 0 0 1 4 0V4" stroke="#9aa" fill="none"/></svg></div>
  <div class="abs btn slate" style="top:183px">Login</div>
  <div class="abs btn teal" style="top:208px">Signup</div>
</section>

<section class="screen row-top" style="left:277px" aria-label="About">
  <div class="status"><span>●●●○○ LUMA</span><span>4:21 PM</span><span>22%<i class="battery"></i></span></div>
  <div class="brand"><span>فانوس‌آرام</span><span class="dot"></span></div>
  <div class="abs center" style="top:66px"><div class="title" style="font-size:8px">Location Based Service</div>
    <div style="font-size:4.5px;color:var(--ink-soft)">CREATING INNOVATIVE APPS AND GAMES</div></div>
  <p class="abs para" style="top:84px">Maecenas condimentus blandit auctor aliquet, urna nibh aliquet tellusd aliquam urna magna in lacusper suscipit purus quis elementud at nisl quismi tristique biben quis justo sit amet metus iaculis semper quisnec urnaroin auctor tempus diameget imperdietpien ullamcorper non. Nunc mauris estmollis vitaemonsequat, posuere lob-ortis odiauris etcongue nunc, quis venenatis dolorroin sagittis mauris augue, vitae commodo mcondentum sednibliget tellusd aliquam una-magnnisuism tristiqued.</p>
  <div style="position:absolute;left:52px;top:164px;width:34px;height:34px;border-radius:50%;background:var(--slate)"></div>
  <div class="abs cards" style="top:209px"><span></span><span></span><span></span></div>
  <div class="abs center" style="top:234px;font-size:4.5px;color:var(--ink)">© 2017 <b>The Quiet Lantern</b> All Rights Reserved</div>
</section>

<section class="screen row-top" style="left:447px" aria-label="Map home">
  <div class="status"><span>●●●○○ LUMA</span><span>4:21 PM</span><span>22%<i class="battery"></i></span></div>
  <div class="map" style="top:10px;height:98px" role="img" aria-label="City map with a magnifying glass over the user's area"></div>
  <div class="abs" style="top:116px;left:14px;width:111px;height:16px;background:var(--paper);border:0.6px solid #9bb">
    <div style="position:absolute;right:0;top:0;width:14px;height:15px;background:var(--slate)">
      <svg width="14" height="15" viewBox="0 0 14 15"><circle cx="6.5" cy="7" r="3" stroke="#fff" fill="none" stroke-width="1.2"/><path d="M8.7 9.2L11 11.5" stroke="#fff" stroke-width="1.2"/></svg></div></div>
  <div class="abs bar" style="top:138px;left:14px;width:111px">Categories</div>
  <div class="abs" style="top:152px;left:14px;width:111px;height:50px;background:#4b6a74"></div>
  <div class="abs btn teal" style="top:218px;left:14px;width:111px">Live Geo Location</div>
</section>

<section class="screen row-top" style="left:618px" aria-label="Profile">
  <div class="status"><span>●●●○○ LUMA</span><span>4:21 PM</span><span>22%<i class="battery"></i></span></div>
  <div class="map" style="top:10px;height:80px" role="img" aria-label="Map background with magnifying glass"></div>
  <svg style="position:absolute;left:5px;top:14px" width="12" height="8" viewBox="0 0 12 8"><path d="M0 1H12M0 4H12M0 7H12" stroke="#fff" stroke-width="1"/></svg>
  <svg style="position:absolute;right:6px;top:14px" width="7" height="7" viewBox="0 0 7 7"><circle cx="3.5" cy="3.5" r="2.5" stroke="#fff" fill="none" stroke-width="1"/></svg>
  <div class="photo" style="left:31px;top:56px;width:76px;height:76px;border-radius:50%;border:3px solid #fff" role="img" aria-label="Profile photo of the user"></div>
  <div class="abs center" style="top:145px;font-size:10px;font-weight:700;color:#2d7f78">ALEX MORROW</div>
  <p class="abs para center" style="top:159px;color:#4a9f95">Maecenas condimentus blandit auctor aliquet, urna nibh aliquet tellusd aliquam urna magna in lacusper suscipit purus quis</p>
  <div class="abs" style="top:187px;left:0;width:138px;border-top:0.6px solid #aacfca"></div>
  <div class="abs stats" style="top:193px"><div><b>FOLLOWERS</b><strong>1890</strong></div><div><b>FOLLOWING</b><strong>2560</strong></div></div>
  <div class="abs btn teal" style="top:218px;left:14px;width:111px">Follow Me</div>
</section>

<section class="screen row-top" style="left:788px" aria-label="Featured">
  <div class="status"><span>●●●○○ LUMA</span><span>4:21 PM</span><span>22%<i class="battery"></i></span></div>
  <div class="map" style="top:10px;height:60px" role="img" aria-label="Map background with magnifying glass"></div>
  <div style="position:absolute;left:54px;top:37px;width:30px;height:30px;border-radius:50%;background:var(--slate);border:2px solid #fff"></div>
  <div class="abs center" style="top:85px"><div class="title" style="font-size:8.5px">Featured</div><div style="font-size:5px;color:var(--ink-soft)">SEARCH LIST</div></div>
  <div class="feat" style="top:110px"><div class="ico"><i></i></div><p>Maecenas conde lipsulipsum ntlandimt auctoqmuet, urnanmibqonde lipsulipsum ntlanditiquet, urnanibqtellusd.</p></div>
  <div class="feat" style="top:134px"><div class="ico"><i></i></div><p>Maecenas conde lipsulipsum ntlandimt auctoqmuet, urnanmibqonde lipsulipsum ntlanditiquet, urnanibqtellusd.</p></div>
  <div class="feat" style="top:158px"><div class="ico"><i></i></div><p>Maecenas conde lipsulipsum ntlandimt auctoqmuet, urnanmibqonde lipsulipsum ntlanditiquet, urnanibqtellusd.</p></div>
  <div class="abs btn teal" style="top:196px;height:19px;line-height:19px">Discount Event at Home</div>
  <div class="abs btn teal" style="top:220px;height:19px;line-height:19px">Send Notifications</div>
</section>

<section class="screen row-top" style="left:961px" aria-label="Point types">
  <div class="status"><span>●●●○○ LUMA</span><span>4:21 PM</span><span>22%<i class="battery"></i></span></div>
  <div class="abs head" style="top:14px">POINT TYPES</div>
  <div class="abs bar" style="top:31px">Location:</div>
  <div class="abs list" style="top:46px"><span>Resturants</span><span>Oil Stations</span><span>Hospitals</span><span>Parks Museums</span><span>Cinema Theatres</span></div>
  <div class="abs bar" style="top:97px">Events:</div>
  <div class="abs list" style="top:111px"><span>Movies</span><span>Theares</span><span>Conferences</span><span>Birthday Party</span><span>Music Show</span></div>
  <div class="abs bar" style="top:163px">Events:</div>
  <div class="abs list" style="top:178px"><span>Taxi Drivers</span><span>Painters</span><span>Technician</span><span>Doctors</span></div>
  <div class="abs btn teal" style="top:220px">Send Now</div>
</section>

<!-- Row 2 -->
<section class="screen row-bottom" style="left:106px" aria-label="Categories">
  <div class="status"><span>●●●○○ LUMA</span><span>4:21 PM</span><span>22%<i class="battery"></i></span></div>
  <div style="position:absolute;top:10px;left:0;width:138px;height:64px;background:radial-gradient(circle at 30% 45%,#9fcfc8,#1f5c5b 55%,#103536)" role="img" aria-label="New year clock artwork with the year 2017"></div>
  <div class="abs head" style="top:68px">CATEGORIES</div>
  <div class="abs cats" style="top:92px"><div>Photo &amp; Video</div><div>Food &amp; Drink</div><div>Games</div><div>Lifestyle</div><div>Entertainment</div><div>Shopping</div><div>Social Network</div><div>Events</div></div>
  <div class="abs btn teal" style="top:220px">Send Now</div>
</section>

<section class="screen row-bottom" style="left:277px" aria-label="Item information">
  <div class="status"><span>●●●○○ LUMA</span><span>4:21 PM</span><span>22%<i class="battery"></i></span></div>
  <div class="abs head" style="top:14px;height:17px;line-height:17px">VIEW ITEM INFORMATION</div>
  <div class="photo abs" style="top:35px;height:81px" role="img" aria-label="Photo of a smartphone lying on a keyboard"></div>
  <div class="abs bar" style="top:121px;height:13px;line-height:13px">Select Categories</div>
  <div class="abs title" style="top:139px;font-size:8px">Main Item Title Here</div>
  <p class="abs para" style="top:150px">Maecenas condimentus blandit auctor aliquet, urna nibh aliquet tellusd aliquam urnamagna nlacuper suscip-it purus quis elementud atnisl quismi tristique biben quis justo sit amet metus iaculis semper quisnec urn-aroin auctordietpien ullamcorpered.</p>
  <div class="abs trio" style="top:186px"><div>PHONE</div><div>EMAIL</div><div>SCHEDULE</div></div>
  <div class="abs bar" style="top:202px;text-align:center;font-size:5px;font-weight:400;padding:0">CLICK TO TAG HERE</div>
  <div class="abs btn teal" style="top:219px">Add to Cart</div>
</section>

<section class="screen row-bottom" style="left:447px" aria-label="Partners">
  <div class="status"><span>●●●○○ LUMA</span><span>4:21 PM</span><span>22%<i class="battery"></i></span></div>
  <div class="abs head" style="top:12px">PARTNERS</div>
  <div class="abs bar" style="top:30px">New Location &amp; Event</div>
  <div class="abs bar light" style="top:46px;height:9px;line-height:9px;font-weight:400">Select Categories</div>
  <div class="abs title" style="top:58px;font-size:7.5px;padding-left:4px">Partner Title Here</div>
  <div class="photo abs" style="top:70px;height:130px" role="img" aria-label="Photo of a smartphone lying on a keyboard"></div>
  <div class="abs trio" style="top:204px"><div>PHONE</div><div>EMAIL</div><div>ADDRESS</div></div>
  <div class="abs btn teal" style="top:219px">Start &amp; End Date</div>
</section>

<section class="screen row-bottom" style="left:618px" aria-label="Rewards">
  <div class="status"><span>●●●○○ LUMA</span><span>4:21 PM</span><span>22%<i class="battery"></i></span></div>
  <div class="abs head" style="top:12px">REWARDS</div>
  <div class="abs bar" style="top:30px">New Location &amp; Event</div>
  <div class="abs bar" style="top:46px">Archive (List):</div>
  <div class="abs list" style="top:61px"><span>Category</span><span>Approved</span><span>Rejected</span><span>Rewarded</span></div>
  <div class="abs bar" style="top:109px">State:</div>
  <div class="abs list" style="top:124px"><span>Reading</span><span>Approved</span><span>Rejected</span><span>Rewarded</span></div>
  <div class="abs bar" style="top:167px">Summary:</div>
  <div class="abs list" style="top:182px"><span>Unused Rewards Sum</span><span>Used Rewards Sum</span><span>Total</span></div>
  <div class="abs btn teal" style="top:219px">Send Now</div>
</section>

<section class="screen row-bottom" style="left:788px" aria-label="Search">
  <div class="status"><span>●●●○○ LUMA</span><span>4:21 PM</span><span>22%<i class="battery"></i></span></div>
  <div class="abs head" style="top:12px">SEARCH</div>
  <div class="abs bar" style="top:30px">Sample Search</div>
  <div class="abs fields dark" style="top:46px;padding-top:2px"><div class="field" style="height:16px;line-height:16px">Point Type</div><div class="field" style="height:16px;line-height:16px">Distance</div><div class="field" style="height:16px;line-height:16px">Start Date</div><div class="field" style="height:16px;line-height:16px">End Date</div><div class="field" style="height:15px;line-height:15px">Categories</div></div>
  <div class="abs bar" style="top:132px">Advanced Search</div>
  <div class="abs" style="top:146px;height:70px;background:#6b9ca1;font-size:5.5px;color:#fff;padding:4px 6px">Query String</div>
  <div class="abs btn teal" style="top:219px">Sort Now</div>
</section>

<section class="screen row-bottom" style="left:961px" aria-label="Search on map">
  <div class="status"><span>●●●○○ LUMA</span><span>4:21 PM</span><span>22%<i class="battery"></i></span></div>
  <div class="abs head" style="top:12px">SEARCH</div>
  <div class="map abs" style="top:31px;height:45px" role="img" aria-label="Map with magnifying glass over search area"></div>
  <div class="abs bar" style="top:82px">Search List</div>
  <div class="abs fields tealish" style="top:98px"><div class="field" style="height:16px;line-height:16px">Point Type</div><div class="field" style="height:16px;line-height:16px">Scrolling Comments</div><div class="field" style="height:16px;line-height:16px">Click on items</div></div>
  <div class="abs bar" style="top:150px">Item Data</div>
  <div class="abs fields tealish" style="top:166px"><div class="field" style="height:16px;line-height:16px">Distance</div><div class="field" style="height:16px;line-height:16px">Title</div><div class="field" style="height:18px;line-height:16px">Category</div></div>
  <div class="abs btn slate" style="top:219px">Search Now</div>
</section>

</body>
</html>
```